Mirabo & Orvan Automotive Repair Shop. Need a new website design.

We specialize in Mirabo & Orvan auto repair, but also work on other Asian import vehicles. We have been in business for 7 years and pride ourselves on high quality auto repair that is fixed right the first time. Would like the automotive repair website to incorporate the colors black, red and white if possible and have our logo and some Mirabo and Orvan vehicles included in the website.

Target Market(s)

Mirabo & Orvan vehicle owners

Industry/Entity Type

Automotive Repair

Coding

Coded - Design and coding required

Number of Pages Required

5+ page

Colors
EB3D1F
EC4F4E
F09395
F8D3D4
FCEDEE

Requirements
Must have
• Home, Services, Contact Us, Schedule appointment, and a gallery tab that I can add shop pictures to when completed.
Nice to have
• Would like to see example pictures of job next to each service listed.
Should not have
• Service not related to auto repair. Ex. auto detailing, towing, car wash

```html
<!DOCTYPE html>
<html lang="en">
<head>
<meta charset="utf-8">
<title>Kestrel Automotive</title>
<link href="https://fonts.googleapis.com/css2?family=Poppins:wght@300;400;500;600;700&display=swap" rel="stylesheet">
<style>
:root{
  --red:#EB3D1F; --red2:#EC4F4E; --rose:#F09395; --blush:#F8D3D4; --pale:#FCEDEE;
  --black:#000; --dark:#333; --grey:#7f7f7f; --text:#444; --muted:#8a8a8a; --white:#fff;
}
*{box-sizing:border-box;margin:0;padding:0}
html,body{width:1200px;height:3293px;overflow:hidden;background:#fff;font-family:'Poppins',sans-serif;color:var(--text)}
.page{position:relative;width:937px;margin-left:133px;height:3293px}
section,header,footer{position:relative;width:937px}
.ph{display:block}
/* hero */
.hero{height:365px;background:linear-gradient(180deg,#3b3f44 0%,#6d7075 45%,#9a9a98 75%,#5c5c5a 100%)}
.nav{position:absolute;top:0;left:0;width:937px;height:59px;background:var(--black)}
.nav-item{position:absolute;top:16px;width:140px;margin-left:-70px;text-align:center;color:#fff;font-size:6.5px;letter-spacing:.2px;white-space:nowrap}
.nav-item svg{display:block;margin:0 auto 4px}
.nav-phone{position:absolute;top:17px;left:676px;color:#fff;font-size:7px;display:flex;gap:8px;align-items:center}
.nav-phone span{color:#555}
.brand-top{position:absolute;top:17px;left:30px;color:#fff;font-weight:700;font-size:16px;display:flex;align-items:center;gap:8px}
.brand-top i{width:14px;height:14px;border-radius:50%;background:var(--red);display:block}
.hero-intro{position:absolute;top:96px;left:61px;width:376px;color:#fff;font-size:11px;line-height:16px}
.badge-round{position:absolute;left:126px;top:172px;width:110px;height:110px;border-radius:50%;background:#2d7fc9;opacity:.9}
.badge-best{position:absolute;left:658px;top:70px;width:90px;height:76px;background:#cfd3d6;border-radius:6px}
.hero-card{position:absolute;left:445px;top:151px;width:486px;height:180px;background:rgba(226,45,45,.82);color:#fff;font-size:10.6px;line-height:16.6px;padding:24px 20px 0 20px;text-align:justify}
/* payment */
.pay{height:152px;background:var(--red2);overflow:hidden}
.pay-dark{position:absolute;left:0;top:0;width:937px;height:152px}
.pay-brand{position:absolute;left:194px;top:30px;color:#2faf57;font-weight:600;font-size:17px;display:flex;align-items:center;gap:6px}
.pay-brand i{width:18px;height:18px;border:2px solid #2faf57;border-radius:50%;display:block}
.pay-note{position:absolute;left:82px;top:64px;color:#ddd;font-size:13px;font-weight:300}
.pay-logo{position:absolute;left:610px;top:56px;color:#fff;font-weight:700;font-size:24px;display:flex;align-items:center;gap:10px}
.pay-logo i{width:22px;height:22px;border-radius:50%;background:#fff;display:block}
/* installer */
.installer{height:212px}
.installer h2{position:absolute;left:34px;top:16px;font-size:20px;font-weight:500;color:#222}
.partner{position:absolute;font-weight:700;font-size:22px;color:var(--red)}
.jug{position:absolute;top:55px;width:80px;height:122px;border-radius:8px;background:linear-gradient(180deg,#c5c9cc,#8e9397)}
.jug.red{background:linear-gradient(180deg,#d33a34,#2a2a2a)}
.batt{position:absolute;top:62px;width:86px;height:102px;background:linear-gradient(135deg,#222,#555 60%,#2a3f8f)}
/* makes */
.makes{height:490px;background:var(--pale);border-top:2px solid var(--blush);border-bottom:2px solid var(--blush);padding:22px 0 0 34px}
.makes h2{font-size:28px;font-weight:500;color:#111;line-height:36px}
.makes .sub{font-size:13.5px;font-weight:300;color:var(--red2);margin-top:2px}
.grid4{display:grid;grid-template-columns:repeat(4,203px);column-gap:18px}
.make-grid{margin-top:8px;row-gap:12px}
.make .ph{height:124px;box-shadow:0 3px 6px rgba(0,0,0,.25)}
.make h3{font-size:9.5px;font-weight:400;color:#333;margin-top:4px}
.make p{font-size:10.5px;font-weight:300;color:var(--muted);line-height:16px}
.more{font-size:10px;color:var(--muted)}
/* services */
.services{height:815px;padding:30px 0 0 34px}
.services h2{font-size:28px;font-weight:500;color:var(--grey);line-height:34px}
.svc-grid{margin-top:4px;row-gap:30px;align-items:start}
.svc .ph{height:114px;box-shadow:0 3px 6px rgba(0,0,0,.3)}
.svc span{display:block;font-size:11.5px;font-weight:300;color:#555;line-height:15px;margin-top:1px}
.btn-outline{display:inline-flex;align-items:center;gap:8px;margin:18px 0 0 6px;width:319px;height:36px;border:2px solid #111;border-radius:2px;padding-left:36px;font-size:11px;color:#222}
/* contact */
.contact{height:352px}
.contact .rule{position:absolute;left:34px;top:10px;width:868px;height:1px;background:#ccc}
.contact-brand{position:absolute;left:112px;top:150px;font-size:26px;font-weight:700;color:var(--red);display:flex;align-items:center;gap:10px}
.contact-brand i{width:22px;height:22px;background:#111;display:block}
.form{position:absolute;left:437px;top:40px;width:426px}
.form h2{font-size:22px;font-weight:500;color:#222;margin-bottom:12px}
.field{height:26px;border:1px solid #ccc;border-radius:3px;font-size:10px;color:#777;padding:5px 9px;margin-bottom:17px}
.field.area{height:60px}
.submit{display:inline-block;background:#111;color:#fff;font-size:10px;padding:4px 10px;border-radius:3px;margin-top:-2px}
/* schedule */
.schedule{height:166px;background:var(--grey);color:#fff}
.schedule h2{position:absolute;left:34px;top:20px;font-size:28px;font-weight:700;line-height:34px;color:#f2f2f2}
.schedule .btn{position:absolute;left:34px;top:94px;width:139px;height:33px;border:1.5px solid #ddd;font-size:11px;display:flex;align-items:center;justify-content:center;gap:8px;color:#eee}
.schedule h3{position:absolute;left:402px;top:56px;font-size:19px;font-weight:500;color:#eee}
.schedule p{position:absolute;left:402px;top:90px;width:500px;font-size:11px;line-height:17px;color:#eee;font-weight:300}
/* gallery */
.gallery{height:498px}
.gallery h2{position:absolute;left:34px;top:28px;font-size:30px;font-weight:700;color:#111;line-height:40px}
.sel{position:absolute;left:34px;top:82px;width:125px;height:28px;background:#000;color:#fff;font-size:10.5px;padding:7px 10px}
.sel b{position:absolute;right:10px;top:8px;font-size:8px}
.year{position:absolute;left:255px;top:84px;font-size:10.5px;color:#555;display:flex;gap:4px}
.year i{display:block;width:140px;height:18px;border:1px solid #888}
.search{position:absolute;left:497px;top:83px;width:139px;height:26px;background:#000;color:#fff;font-size:11px;display:flex;align-items:center;justify-content:center;gap:8px}
.gcard{position:absolute;top:131px;width:164px}
.gthumb{height:140px;background:#111;position:relative;box-shadow:0 3px 6px rgba(0,0,0,.3)}
.gthumb span{position:absolute;left:0;bottom:0;width:100%;height:34px;background:#555;color:#ddd;font-weight:700;font-size:16px;text-align:center;line-height:34px;letter-spacing:1px}
.gcard h3{font-size:14px;font-weight:700;color:#222;margin-top:6px}
.gcard h4{font-size:8px;font-weight:700;color:#555;margin-top:2px}
.gcard p{font-size:8px;color:#777;line-height:12.5px;font-weight:300}
.pager{position:absolute;top:379px;left:48px;display:flex;align-items:center;font-size:11px;color:#444}
.pager span{width:48px;text-align:center}
.pager .on{background:#555;color:#fff;height:26px;line-height:26px;width:46px;margin:0 6px}
/* footer */
.footer{height:242px;background:#000;color:#fff}
.foot-brand{position:absolute;left:60px;top:96px;font-size:16px;font-weight:700;color:var(--red);display:flex;align-items:center;gap:8px;white-space:nowrap}
.foot-brand i{width:12px;height:12px;border-radius:50%;background:#fff;display:block}
.fcol{position:absolute;top:50px;font-size:9.5px;line-height:15px}
.fcol h4{font-size:9px;font-weight:600;margin-bottom:2px}
.fcol .row{display:flex;align-items:center;gap:5px}
.social{display:flex;gap:10px;margin-top:10px;font-size:9px}
.social span{display:flex;align-items:center;gap:3px}
.social i{width:8px;height:8px;border-radius:50%;background:#fff;display:block}
.copy{position:absolute;left:82px;top:208px;font-size:8.5px;color:#ddd}
.copy b{font-weight:600}
</style>
</head>
<body>
<div class="page">

<header class="hero">
  <div class="ph" role="img" aria-label="Photo of the shop front with Mirabo and Orvan SUVs parked in the service bays" style="position:absolute;inset:59px 0 0 0"></div>
  <nav class="nav">
    <div class="brand-top"><i></i>Kestrel Automotive</div>
    <div class="nav-item" style="left:292px"><svg width="14" height="13" viewBox="0 0 14 13"><path d="M7 0L0 6h2v7h4V9h2v4h4V6h2z" fill="#fff"/></svg>HOME</div>
    <div class="nav-item" style="left:346px"><svg width="14" height="13" viewBox="0 0 14 13"><path d="M1 1l12 11M13 1L1 12" stroke="#fff" stroke-width="2.4"/></svg>SERVICES</div>
    <div class="nav-item" style="left:411px"><svg width="15" height="12" viewBox="0 0 15 12"><rect x="0.5" y="0.5" width="14" height="11" rx="1.5" fill="#fff"/><rect x="2.5" y="3" width="4" height="4" fill="#000"/><path d="M8 4h5M8 7h5" stroke="#000"/></svg>CONTACT US</div>
    <div class="nav-item" style="left:507px"><svg width="13" height="13" viewBox="0 0 13 13"><rect x="0" y="2" width="13" height="11" rx="1" fill="#fff"/><path d="M2 6h9M2 9h9M4.5 5v7M8.5 5v7" stroke="#000" stroke-width=".8"/></svg>SCHEDULE AN APPOINTMENT</div>
    <div class="nav-item" style="left:597px"><svg width="11" height="13" viewBox="0 0 11 13"><path d="M0 0h7l4 4v9H0z" fill="#fff"/><path d="M2 7h7M2 10h7" stroke="#000"/></svg>GALLERY</div>
    <div class="nav-item" style="left:643px"><svg width="11" height="12" viewBox="0 0 11 12"><circle cx="5.5" cy="3.5" r="3" fill="none" stroke="#fff"/><path d="M0.5 12c0-4 10-4 10 0" fill="none" stroke="#fff"/></svg></div>
    <div class="nav-phone"><svg width="11" height="11" viewBox="0 0 11 11"><path d="M2 0l2 2.5-1.2 1.5c.8 1.6 2 2.8 3.6 3.6L8 6.4 11 8.5 9.5 11C4 10.5.5 7 0 1.5z" fill="#fff"/></svg><span>+00 000 000 00</span></div>
  </nav>
  <div class="badge-round" role="img" aria-label="Certification badge"></div>
  <p class="hero-intro">Kestrel Automotive is a locally owned and operated auto repair shop in Brookdale that offers comprehensive car care and services for Mirabo &amp; Orvan and all other Asian imports vehicles</p>
  <div class="badge-best" role="img" aria-label="Best of Brookdale award badge"></div>
  <div class="hero-card">Led by an NTA master certified technician with 20 years experience working for Mirabo &amp; Orvan dealerships, our auto shop is your go to facility for everything from factory auto maintenance, including oil changes, fluid services and tune ups, to complex engine repairs, hybrid diagnostic &amp; repair, brake jobs, etc. We have state of the art equipment and tools to ensure that we can properly diagnose and repair your vehicle to get you back on the road. Our work comes with a warranty and we offer towing if needed. We also offer discounts for Ridego &amp; Hoplift rides.</div>
</header>

<section class="pay">
  <svg class="pay-dark" viewBox="0 0 937 152" width="937" height="152"><polygon points="0,0 461,0 417,152 0,152" fill="#333"/></svg>
  <div class="pay-brand"><i></i>Paywell</div>
  <p class="pay-note">We accept payments with Paywell transactions</p>
  <div class="pay-logo"><i></i>Kestrel Automotive</div>
</section>

<section class="installer">
  <h2>Authorized installer for Veltra Oil, Ironway Battery</h2>
  <div class="partner" style="left:40px;top:60px">Veltra Oil</div>
  <div class="partner" style="left:104px;top:100px;color:#111">Ironway Batteries</div>
  <div class="jug" role="img" aria-label="Synthetic motor oil jug" style="left:337px"></div>
  <div class="jug red" role="img" aria-label="Synthetic motor oil jug" style="left:430px"></div>
  <div class="jug" role="img" aria-label="European formula motor oil jug" style="left:520px"></div>
  <div class="batt" role="img" aria-label="Car battery installed in engine bay" style="left:626px"></div>
  <div class="batt" role="img" aria-label="Battery replacement under the hood" style="left:721px;background:linear-gradient(135deg,#888,#ddd 50%,#444)"></div>
  <div class="batt" role="img" aria-label="New battery in engine bay" style="left:814px"></div>
</section>

<section class="makes">
  <h2>Kestrel Automotive</h2>
  <p class="sub">Specializes in Mirabo &amp; Orvan auto repair but also service and repair the following makes: (Emblems)</p>
  <div class="grid4 make-grid">
    <div class="make"><div class="ph" role="img" aria-label="Blue convertible parked outdoors" style="background:linear-gradient(180deg,#a88a66,#2c4ea8 60%,#6b5a44)"></div><h3>HANZO</h3><p>Description: lorem ipsum Lorem ipsum Lorem ipsum Lorem ipsum</p></div>
    <div class="make"><div class="ph" role="img" aria-label="Red crossover in a showroom" style="background:linear-gradient(180deg,#444,#b52b2b 55%,#666)"></div><h3>ACURIO</h3><p>Description: lorem ipsum Lorem ipsum Lorem ipsum Lorem ipsum</p></div>
    <div class="make"><div class="ph" role="img" aria-label="White sedan front view" style="background:linear-gradient(180deg,#555,#d8d8d8 55%,#777)"></div><h3>NISEMA</h3><p>Description: lorem ipsum Lorem ipsum Lorem ipsum Lorem ipsum</p></div>
    <div class="make"><div class="ph" role="img" aria-label="Black luxury SUV in a showroom" style="background:linear-gradient(180deg,#e8e8e8,#222 55%,#ccc)"></div><h3>INFORA</h3><p>Description: lorem ipsum Lorem ipsum Lorem ipsum Lorem ipsum</p></div>
    <div class="make"><div class="ph" role="img" aria-label="Grey compact SUV in a field" style="background:linear-gradient(180deg,#b7a98a,#6d6d6d 60%,#4b5a2a)"></div><h3>HYRUN</h3><p>Description: lorem ipsum Lorem ipsum Lorem ipsum Lorem ipsum</p><span class="more">More info →</span></div>
    <div class="make"><div class="ph" role="img" aria-label="Red hatchback on display" style="background:linear-gradient(180deg,#8fa4c8,#b3202a 60%,#5a6a8a)"></div><h3>KITO</h3><p>Description: lorem ipsum Lorem ipsum Lorem ipsum Lorem ipsum</p><span class="more">More info →</span></div>
    <div class="make"><div class="ph" role="img" aria-label="Rally car kicking up dirt" style="background:linear-gradient(180deg,#b9a268,#7c7c7c 55%,#a98555)"></div><h3>MITSURI</h3><p>Description: lorem ipsum Lorem ipsum Lorem ipsum Lorem ipsum</p><span class="more">More info →</span></div>
    <div class="make"><div class="ph" role="img" aria-label="White hatchback front view" style="background:linear-gradient(180deg,#4d6a3a,#eeeeee 55%,#333)"></div><h3>MAZERU</h3><p>Description: lorem ipsum Lorem ipsum Lorem ipsum Lorem ipsum</p><span class="more">More info →</span></div>
  </div>
</section>

<section class="services">
  <h2>Services</h2>
  <div class="grid4 svc-grid">
    <div class="svc"><div class="ph" role="img" aria-label="Oil change under a lifted car" style="background:linear-gradient(180deg,#6a7a8a,#3a4a6a 50%,#a33)"></div><span>Oil Changes</span></div>
    <div class="svc"><div class="ph" role="img" aria-label="Car on lift for computer diagnostics" style="background:linear-gradient(180deg,#777,#cfd3d6 60%,#555)"></div><span>Computer Diagnostics</span></div>
    <div class="svc"><div class="ph" role="img" aria-label="Technician working in an engine bay" style="background:linear-gradient(180deg,#2a2a2a,#6a6a6a 60%,#333)"></div><span>Electrical Specialists</span></div>
    <div class="svc"><div class="ph" role="img" aria-label="Wheel removed on lifted car" style="background:linear-gradient(180deg,#8a8a8a,#555 60%,#999)"></div><span>Tires</span></div>
    <div class="svc"><div class="ph" role="img" aria-label="Tire balancing on lifted car" style="background:linear-gradient(180deg,#999,#4a4a4a 60%,#888)"></div><span>Tire Balance &amp; Rotations</span></div>
    <div class="svc"><div class="ph" role="img" aria-label="Engine bay inspection" style="background:linear-gradient(180deg,#1e2a3a,#4a5a6a 55%,#222)"></div><span>Pre Purchase Inspections</span></div>
    <div class="svc"><div class="ph" role="img" aria-label="Technician repairing a damaged part" style="background:linear-gradient(180deg,#333,#8a2a2a 60%,#222)"></div><span>Insurance Claims</span></div>
    <div class="svc"><div class="ph" role="img" aria-label="Exhaust and catalytic converter work under a car" style="background:linear-gradient(180deg,#aaa,#5a5a5a 60%,#888)"></div><span>Emission Repair &amp; Catalytic Converters</span></div>
    <div class="svc"><div class="ph" role="img" aria-label="Engine block being rebuilt" style="background:linear-gradient(180deg,#ccc,#444 55%,#999)"></div><span>Engine Repair</span></div>
    <div class="svc"><div class="ph" role="img" aria-label="Engine bay for AC service" style="background:linear-gradient(180deg,#1e2a3a,#4a5a6a 55%,#222)"></div><span>Heating &amp; AC Repair</span></div>
    <div class="svc"><div class="ph" role="img" aria-label="Engine bay for state inspection" style="background:linear-gradient(180deg,#1e2a3a,#4a5a6a 55%,#222)"></div><span>State Inspection</span></div>
    <div class="svc"><div class="ph" role="img" aria-label="Suspension work on lifted car" style="background:linear-gradient(180deg,#555,#8a7a6a 60%,#444)"></div><span>Suspension Service &amp; Repair</span></div>
    <div class="svc"><div class="ph" role="img" aria-label="Lift kit installation under a truck" style="background:linear-gradient(180deg,#555,#8a7a6a 60%,#444)"></div><span>Leveling Kits &amp; Minor Lift Kit installation</span></div>
    <div class="svc"><div class="ph" role="img" aria-label="Brake rotor and clutch parts" style="background:linear-gradient(180deg,#3a3a3a,#6a6a6a 60%,#2a2a2a)"></div><span>Brakes Service &amp; Repair</span></div>
    <div class="svc"><div class="ph" role="img" aria-label="Exhaust system work in the shop" style="background:linear-gradient(180deg,#888,#5a5a5a 60%,#999)"></div><span>Exhaust, Muffler Service &amp; Repair</span></div>
    <div class="svc"><div class="ph" role="img" aria-label="Car on lift in the shop for transmission service" style="background:linear-gradient(180deg,#6a8a9a,#cfd8dd 60%,#3a5a8a)"></div><span>Automatic, Manual, Computerized Transmission Service &amp; Repair</span></div>
  </div>
  <div class="btn-outline">Dont see a service you need? Contact us <svg width="10" height="8" viewBox="0 0 10 8"><path d="M0 4h8M5 1l3 3-3 3" stroke="#111" stroke-width="1.4" fill="none"/></svg></div>
</section>

<section class="contact">
  <div class="rule"></div>
  <div class="contact-brand"><i></i>Kestrel Automotive</div>
  <div class="form">
    <h2>Contact Us</h2>
    <div class="field">Name</div>
    <div class="field">Phone</div>
    <div class="field">email</div>
    <div class="field area">How can we help?</div>
    <span class="submit">Submit</span>
  </div>
</section>

<section class="schedule">
  <h2>Schedule an<br>appointment</h2>
  <div class="btn">See more <svg width="10" height="8" viewBox="0 0 10 8"><path d="M0 4h8M5 1l3 3-3 3" stroke="#eee" stroke-width="1.4" fill="none"/></svg></div>
  <h3>Title</h3>
  <p>lorem ipsum lorem ipsum lorem ipsum lorem ipsum lorem ipsum lorem ipsum lorem ipsum lorem ipsum lorem ipsum lorem ipsum lorem ipsum lorem ipsum lorem ipsum lorem ipsum lorem ipsum lorem ipsum lorem ipsum</p>
</section>

<section class="gallery">
  <h2>Gallery</h2>
  <div class="sel">Select car: <b>▼</b></div>
  <div class="year">Year : <i></i></div>
  <div class="search"><svg width="10" height="10" viewBox="0 0 10 10"><circle cx="4" cy="4" r="3" stroke="#fff" stroke-width="1.5" fill="none"/><path d="M6.3 6.3L9.5 9.5" stroke="#fff" stroke-width="1.5"/></svg>Search</div>
  <div class="gcard" style="left:55px"><div class="gthumb" role="img" aria-label="Gallery cover"><span>GALLERY</span></div><h3>Gallery 1</h3><h4>Details gallery</h4><p>Lorem ipsum dolor sit amet, consectetur adipiscing elit, sed do eiusmod tempor incididunt ut labore et dolore magna aliqua.</p></div>
  <div class="gcard" style="left:276px"><div class="gthumb" role="img" aria-label="Gallery cover"><span>GALLERY</span></div><h3>Gallery 2</h3><h4>Details gallery</h4><p>Lorem ipsum dolor sit amet, consectetur adipiscing elit, sed do eiusmod tempor incididunt ut labore et dolore magna aliqua.</p></div>
  <div class="gcard" style="left:497px"><div class="gthumb" role="img" aria-label="Gallery cover"><span>GALLERY</span></div><h3>Gallery 3</h3><h4>Details gallery</h4><p>Lorem ipsum dolor sit amet, consectetur adipiscing elit, sed do eiusmod tempor incididunt ut labore et dolore magna aliqua.</p></div>
  <div class="gcard" style="left:718px"><div class="gthumb" role="img" aria-label="Gallery cover"><span>GALLERY</span></div><h3>Gallery 4</h3><h4>Details gallery</h4><p>Lorem ipsum dolor sit amet, consectetur adipiscing elit, sed do eiusmod tempor incididunt ut labore et dolore magna aliqua.</p></div>
  <div class="pager"><span>«</span><span class="on">1</span><span>2</span><span>3</span><span>4</span><span>5</span><span>6</span><span>»</span></div>
</section>

<footer class="footer">
  <div class="foot-brand"><i></i>Kestrel Automotive</div>
  <div class="fcol" style="left:278px"><h4>Address</h4>lorem ipsum<br>lorem ipsum<br>lorem ipsum</div>
  <div class="fcol" style="left:476px"><h4>Contact Us</h4>
    <div class="row"><svg width="8" height="8" viewBox="0 0 8 8"><rect width="8" height="8" rx="1" fill="#fff"/></svg>+00 (41) 000 00 00</div>
    <div class="row"><svg width="8" height="8" viewBox="0 0 11 11"><path d="M2 0l2 2.5-1.2 1.5c.8 1.6 2 2.8 3.6 3.6L8 6.4 11 8.5 9.5 11C4 10.5.5 7 0 1.5z" fill="#fff"/></svg>+00 (41) 000 00 00</div>
    <div class="row"><svg width="7" height="9" viewBox="0 0 7 9"><path d="M3.5 9C1 5.5 0 4.5 0 3.3A3.5 3.3 0 0 1 7 3.3C7 4.5 6 5.5 3.5 9z" fill="#fff"/></svg>Location Map</div>
  </div>
  <div class="fcol" style="left:674px"><h4>Media social</h4>
    <div class="social"><span><i></i>Facely</span><span><i></i>Pixgram</span><span><i></i>Linkora</span></div>
    <div class="social" style="margin-top:4px"><span><i></i>Chirper</span><span><i></i>Vidtube</span></div>
  </div>
  <p class="copy">© Copyright <b>Kestrel Automotive</b>. All Rights Reserved</p>
</footer>

</div>
</body>
</html>
```